Create a web design for a vehicle codes lookup website

Create a bright and fun web design to replace our current boring one!

-Make a new design for this page that shows vehicle codes information: http://plinkor.net/vin/mara-dulek.4182.html
-Click "Random VIN" to see more examples.
-The page shows the vehicle information (see above example) is the most important one to add a redesign to. Bonus points if you create a redesign for the main page as well: plinkor.net.

Number of Pages Required

2 page

Requirements
Must have
• Be fun and have bright colors!
Should not have
• Do not add pictures of specific people or vehicles unless they can be used on every page. The example page has a Brevik Solano, but do not add a picture of the Brevik Solano because other pages have different vehicles.

```html
<!DOCTYPE html>
<html lang="en">
<head>
<meta charset="utf-8">
<title>Plinkor – Vehicle Purchase Records Database</title>
<link href="https://fonts.googleapis.com/css2?family=Open+Sans:wght@400;600;700;800&family=Oswald:wght@500;600&display=swap" rel="stylesheet">
<style>
:root{
  --navy:#17365f;
  --nav:#1d3b66;
  --blue:#1f6cc4;
  --sky:#e9f3fc;
  --red:#d62f2b;
  --text:#5a6470;
  --heading:#1f5fa8;
  --footer:#1e2a38;
  --footer-text:#9aa6b4;
  --line:#dde4ec;
  --white:#ffffff;
}
*{box-sizing:border-box;margin:0;padding:0}
html,body{width:811px;height:1200px;overflow:hidden}
body{font-family:"Open Sans",Arial,sans-serif;background:var(--white);color:var(--text);position:relative}

.site-header{position:absolute;left:0;top:0;width:811px;height:64px;background:var(--white)}
.brand{position:absolute;left:16px;top:12px;display:flex;align-items:center;gap:10px}
.brand-mark{width:40px;height:40px;background:var(--navy);border-radius:4px}
.brand-name{font-weight:700;font-size:22px;line-height:40px;color:var(--navy)}
.social{position:absolute;right:22px;top:20px;display:flex;gap:7px}
.social span{width:22px;height:22px;border-radius:50%;background:#8a96a6}

.main-nav{position:absolute;left:0;top:64px;width:811px;height:34px;background:var(--nav);display:flex;align-items:stretch;padding-left:12px}
.main-nav a{color:var(--white);text-decoration:none;font-size:10.5px;font-weight:600;padding:0 14px;display:flex;align-items:center;letter-spacing:.3px}
.main-nav a.active{background:var(--blue)}
.main-nav a.login{position:absolute;right:14px;top:5px;height:24px;background:var(--blue);border-radius:2px}

.hero{position:absolute;left:0;top:98px;width:811px;height:352px;background:linear-gradient(180deg,#2b74c6 0%,#3d8bd8 62%,#cfe3f5 62%,#eaf3fb 100%)}
.hero-title{position:absolute;left:330px;top:58px;color:var(--white);font-family:"Oswald","Open Sans",sans-serif;font-weight:600;text-transform:uppercase;line-height:1.05}
.hero-title .big{font-size:40px;display:block;letter-spacing:.5px}
.hero-title .small{font-size:31px;display:block}
.hero-car{position:absolute;left:380px;top:170px;width:420px;height:160px;border-radius:80px 120px 20px 20px;background:radial-gradient(ellipse at 50% 40%,#e2e6ea 0%,#b6bec7 55%,#7e8893 100%)}

.quick-search{position:absolute;left:30px;top:118px;width:232px;height:302px;background:var(--white);border-radius:3px;box-shadow:0 3px 10px rgba(0,0,0,.25);padding:16px 16px}
.quick-search h2{font-size:17px;font-weight:800;color:var(--heading);border-left:4px solid var(--blue);padding-left:8px;margin-bottom:16px;letter-spacing:.3px}
.field{height:30px;border:1px solid var(--line);border-radius:2px;font-size:10.5px;color:#8e98a4;padding:0 10px;display:flex;align-items:center;margin-bottom:11px;background:#fafcfe}
.example{font-size:7.5px;color:#98a2ad;margin:-5px 0 14px}
.search-btn{display:block;margin-left:auto;width:110px;height:30px;background:var(--red);color:var(--white);font-size:11px;font-weight:700;border:none;border-radius:2px;letter-spacing:.4px}
.note{font-size:7px;text-align:right;color:#a6afb9;margin-top:6px}

.section-title{position:absolute;left:30px;font-size:22px;font-weight:800;color:var(--heading);letter-spacing:.3px}
.section-title::after{content:"";display:block;width:46px;height:3px;background:var(--red);margin-top:4px}
.about{top:466px}
.about-text{position:absolute;left:30px;top:512px;width:752px;font-size:10.5px;line-height:17px}
.dos{top:604px}

.dos-list{position:absolute;left:30px;top:654px;width:490px;list-style:none}
.dos-list li{height:66px;display:flex;gap:14px}
.dos-list .icon{width:34px;height:34px;flex:none;border-radius:50%;background:var(--sky);display:flex;align-items:center;justify-content:center}
.dos-list h3{font-size:13px;font-weight:700;color:var(--heading);margin:2px 0 3px}
.dos-list p{font-size:9.5px;line-height:13px}

.sample-report{position:absolute;left:548px;top:648px;width:236px;height:222px;border:1px solid var(--line);background:var(--white)}
.sample-report h4{height:28px;background:var(--blue);color:var(--white);font-size:12px;font-weight:700;display:flex;align-items:center;justify-content:center}
.report-body{padding:10px 14px;font-size:7.5px;line-height:11.5px;color:#4b5460}
.report-body b{color:#2b3440}
.ad-banner{position:absolute;left:548px;top:884px;width:236px;height:158px;background:linear-gradient(160deg,#2c2f35 0%,#4b5058 60%,#b3262a 100%)}

.site-footer{position:absolute;left:0;top:1062px;width:811px;height:138px;background:var(--footer);padding:16px 30px;color:var(--footer-text)}
.footer-links{display:flex;gap:16px;font-size:10px;color:#cfd7e0;margin-bottom:8px}
.copyright{font-size:9px;margin-bottom:6px;display:flex;gap:16px}
.disclaimer{font-size:7.5px;line-height:11px}
</style>
</head>
<body>

<header class="site-header">
  <div class="brand">
    <div class="brand-mark"></div>
    <div class="brand-name">Plinkor</div>
  </div>
  <div class="social"><span></span><span></span><span></span></div>
</header>

<nav class="main-nav">
  <a class="active" href="#">HOME</a>
  <a href="#">SEARCH BY OWNER</a>
  <a href="#">VIN LOOKUP</a>
  <a href="#">COMPLETE LIST</a>
  <a href="#">CONTACT US</a>
  <a href="#">RANDOM VIN</a>
  <a class="login" href="#">LOGIN</a>
</nav>

<section class="hero">
  <h1 class="hero-title"><span class="big">Vehicle Purchase</span><span class="small">Records Data Search</span></h1>
  <div class="hero-car" role="img" aria-label="Silver sedan photograph"></div>
</section>

<form class="quick-search">
  <h2>QUICK SEARCH</h2>
  <div class="field">First Name</div>
  <div class="field">Last Name</div>
  <div class="field">Enter Your VIN</div>
  <p class="example">Example: 1HGBH41JXMN109186</p>
  <button class="search-btn" type="button">SEARCH NOW</button>
  <p class="note">*Records are updated daily</p>
</form>

<h2 class="section-title about">WHAT IS PLINKOR.NET?</h2>
<p class="about-text">Plinkor is a website that provides free access to vehicle purchase records data. All information on this website is public information, and as such, we believe it should be free for all to view. The data comes from dealerships and auto insurance companies for new vehicle purchases across the United States. Search by name or by VIN to find vehicle purchase information, vehicle specifics, and fuel economy information.</p>

<h2 class="section-title dos">DO'S AND DONT'S</h2>
<ul class="dos-list">
  <li><span class="icon"><svg width="18" height="18" viewBox="0 0 18 18"><circle cx="9" cy="6" r="3.5" fill="#1f6cc4"/><path d="M2 17c0-4 3-6 7-6s7 2 7 6z" fill="#1f6cc4"/></svg></span>
    <div><h3>Find a Friend</h3><p>Use our reports to find and reconnect with a lost friend.</p></div></li>
  <li><span class="icon"><svg width="18" height="18" viewBox="0 0 18 18"><path d="M3 9l4 4 8-9" stroke="#1f6cc4" stroke-width="2.5" fill="none"/></svg></span>
    <div><h3>Check Yourself Out</h3><p>It's good to know what's out there for your own peace of mind!</p></div></li>
  <li><span class="icon"><svg width="18" height="18" viewBox="0 0 18 18"><path d="M2 9l7-6 7 6v8H2z" fill="#1f6cc4"/></svg></span>
    <div><h3>About your Neighbors</h3><p>Keep your family informed by knowing about the people around you.</p></div></li>
  <li><span class="icon"><svg width="18" height="18" viewBox="0 0 18 18"><rect x="2" y="5" width="14" height="10" rx="1" fill="#1f6cc4"/><rect x="6" y="2" width="6" height="4" fill="none" stroke="#1f6cc4" stroke-width="1.5"/></svg></span>
    <div><h3>Screen Employees</h3><p>You cannot use our reports for employment screening of any kind. We take this very seriously.</p></div></li>
  <li><span class="icon"><svg width="18" height="18" viewBox="0 0 18 18"><circle cx="9" cy="9" r="7" fill="none" stroke="#d62f2b" stroke-width="2"/><path d="M4 14L14 4" stroke="#d62f2b" stroke-width="2"/></svg></span>
    <div><h3>Stalk or Spy</h3><p>Don't stalk, spy on people, or contact them against their wishes.</p></div></li>
  <li><span class="icon"><svg width="18" height="18" viewBox="0 0 18 18"><circle cx="9" cy="9" r="7" fill="none" stroke="#d62f2b" stroke-width="2"/><path d="M4 14L14 4" stroke="#d62f2b" stroke-width="2"/></svg></span>
    <div><h3>Steal an Identity</h3><p>Don't use our information to gather someone's information for any illegal purpose.</p></div></li>
</ul>

<aside class="sample-report">
  <h4>View Sample Report</h4>
  <div class="report-body">
    <b>Customer Name: MARA DULEK</b><br>
    Location: Springfield, Ohio<br>
    Vehicle: 2015 Brevik Solano XLE<br>
    VIN: 4T1BK1EB6FU000000<br>
    Body Style: Sedan 4 Door<br>
    Engine: 3.5L V6 DOHC 24V<br>
    Transmission: 6-Speed Automatic<br>
    Drive Type: Front Wheel Drive<br>
    Fuel Economy City: 21 mpg<br>
    Fuel Economy Highway: 31 mpg<br>
    Exterior Color: Silver<br>
    Purchase Type: New Vehicle<br>
    Source: plinkor.net/vin/mara-dulek.4182
  </div>
</aside>

<div class="ad-banner" role="img" aria-label="Norvale car advertisement with a red sedan"></div>

<footer class="site-footer">
  <nav class="footer-links"><span>Home</span><span>Search by name</span><span>VIN Lookup</span><span>Complete List</span><span>Contact Us</span><span>Random VIN</span></nav>
  <div class="copyright"><span>© Copyright PLINKOR.NET</span><span>Terms</span><span>Privacy</span></div>
  <p class="disclaimer">DISCLAIMER: By using this site, you certify that you will use any information obtained for lawful and permitted purposes. Information contained herein is gathered from records that may have errors and we cannot guarantee its accuracy or completeness. Data is not intended to be used for consumer credit, employment screening, insurance underwriting, or tenant decisions. The records shown are sourced from dealerships and insurers and are updated on a regular basis. All content is provided for informational use only and is subject to change without notice.</p>
</footer>

</body>
</html>
```